Sales sheet for printing and embroidery apparel items - Copper Fern Prints

I would like a one page flyer or sales sheet that I would use as a template to send different images of apparel we produce. I have attached examples of layouts I like.
- Ideally, it would have space for 3-5 items.
- I would like it one page only - not a folding flyer.
- Our companies name is Copper Fern Prints.
- This will be used for many different products and markets so I don't need wording/copy. You can use wording from the 7Q7 or K81 flyer.

Colors
0054AA
0677BA
7BADD7
CADEEF
E8F1F8
00AB8E
00BBA5
67D7C9
C6EFE9
E9F9F6
FFC000
F8CF3A
FAE287
FDF2CF
FEFAEE

Requirements
Must have
• Places for between 3 and 5 images of apparel (t-shirts, hats etc)

```html
<!DOCTYPE html>
<html lang="en">
<head>
<meta charset="utf-8">
<title>Copper Fern Prints – Sample Merch Kit</title>
<link href="https://fonts.googleapis.com/css2?family=Anton&family=Montserrat:ital,wght@0,400;0,500;0,700;0,800;1,500;1,800&display=swap" rel="stylesheet">
<style>
:root{
  --sheet:#f8cf3a;
  --sheet-deep:#ffc000;
  --ink:#161616;
  --panel:#1e1e20;
  --white:#ffffff;
  --accent:#ffc000;
  --alert:#e8584a;
  --photo-bg:#dcdcdc;
  --logo-blue:#0054aa;
}
*{box-sizing:border-box;margin:0;padding:0}
html,body{width:941px;height:1200px;overflow:hidden}
body{font-family:"Montserrat",sans-serif;color:var(--ink);background:var(--sheet)}
.sheet{position:relative;width:941px;height:1200px;background:radial-gradient(ellipse at 50% 40%,#fbd94a 0%,var(--sheet) 60%,#f6c82a 100%);overflow:hidden}
.abs{position:absolute}

.series-tab{left:80px;top:0;width:165px;height:292px;background:linear-gradient(180deg,#000 0%,#1c1c1c 100%);border-radius:0 0 14px 14px;border-top-right-radius:120px 150px;color:var(--white);padding:74px 0 0 20px}
.series-tab .word{font-family:"Anton",sans-serif;font-size:44px;line-height:1;letter-spacing:.5px}
.series-tab .sub{font-size:12px;font-weight:700;line-height:1.25;margin-top:6px}
.series-tab .sub em{font-style:normal;color:var(--accent);display:block}
.series-tab hr{border:0;border-top:1px solid #555;margin:12px 14px 14px -5px}

.masthead{left:260px;top:70px;width:420px;text-align:center}
.masthead .top{font-family:"Anton",sans-serif;font-size:60px;line-height:1}
.masthead .main{font-family:"Anton",sans-serif;font-size:104px;line-height:1;letter-spacing:1px;margin-top:2px}
.masthead .kit{font-weight:800;font-size:24px;letter-spacing:.5px;margin-top:6px}

.warning{left:698px;top:0;width:165px;height:292px;border:1px solid var(--ink);border-top:0;border-radius:0 0 14px 14px;padding:80px 0 0 18px;font-size:12px;line-height:1.38;font-weight:500}
.warning svg{display:block;margin-bottom:8px}
.warning h3{font-weight:800;font-size:14px;letter-spacing:.3px;margin-bottom:5px}

.gallery{left:80px;top:325px;display:flex;gap:14px}
.polaroid{width:185px;height:199px;background:var(--white);padding:6px;box-shadow:0 2px 4px rgba(0,0,0,.25)}
.polaroid .shot{width:100%;height:155px;background:radial-gradient(circle at 50% 45%,#fafafa 0%,var(--photo-bg) 100%);display:flex;align-items:center;justify-content:center}
.polaroid .garment{width:96px;height:118px;border-radius:14px 14px 6px 6px}

.contents{left:82px;top:548px;display:flex;align-items:center}
.contents h2{font-weight:800;font-size:25px;line-height:.98;width:195px}
.item{display:flex;align-items:center;gap:12px;font-size:17px;line-height:1.2;padding:0 22px}
.item+.item{border-left:1px solid var(--ink)}
.item:first-of-type{padding-left:0}
.item .num{width:44px;height:44px;border:1px solid var(--ink);border-radius:50%;display:flex;align-items:center;justify-content:center;font-size:18px;flex:none}

.divider{left:0;top:621px;width:941px;border-top:1px solid var(--ink)}

.how{left:82px;top:652px;width:380px}
.how h2{font-weight:800;font-size:24px;letter-spacing:.3px;white-space:nowrap}
.steps{position:relative;margin-top:30px}
.steps::before{content:"";position:absolute;left:22px;top:44px;height:235px;border-left:1px dashed var(--ink)}
.step{display:flex;gap:18px;margin-bottom:28px}
.step .icon{width:44px;height:44px;border:1px solid var(--ink);border-radius:50%;flex:none;display:flex;align-items:center;justify-content:center;background:var(--sheet)}
.step h3{font-weight:700;font-size:16px;margin:6px 0 10px}
.step p{font-size:14px;line-height:1.32}

.about{left:498px;top:652px;width:360px}
.about h2{font-weight:800;font-size:24px}
.about p{font-size:14px;line-height:1.32;margin-top:12px}

.fine-print{left:493px;top:793px;width:368px;height:165px;background:var(--panel);color:var(--white);padding:22px 26px;clip-path:polygon(0 0,100% 0,100% 62%,82% 100%,0 100%)}
.fine-print h3{font-style:italic;font-weight:800;font-size:14px;margin-bottom:16px}
.fine-print p{font-style:italic;font-weight:500;font-size:11.5px;line-height:1.38}
.page-curl{left:813px;top:896px;width:48px;height:62px;background:linear-gradient(135deg,#4a4a4c 0%,#2b2b2d 100%);clip-path:polygon(100% 0,0 100%,10% 30%)}

.contact{left:493px;top:986px;width:220px}
.contact h3{font-weight:800;font-size:16px;line-height:1.2}
.contact p{font-size:14px;line-height:1.3;margin:12px 0 18px}
.contact .line{display:flex;align-items:center;gap:6px;font-weight:700;font-size:14px;margin-bottom:16px}

.brand-mark{left:712px;top:1005px;width:150px;text-align:center;color:var(--logo-blue);font-weight:800;font-size:22px;line-height:1.05}
.brand-mark .square{width:108px;height:96px;background:var(--logo-blue);margin:0 auto 10px}

.sign-line{left:0;top:1092px;width:451px;border-top:1px solid var(--ink)}
.sign-off{left:80px;top:1117px;font-weight:800;font-size:17px}
</style>
</head>
<body>
<main class="sheet">

  <aside class="abs series-tab">
    <div class="word">MODEL</div>
    <div class="sub"><em>CFP Shop</em>T-shirts</div>
    <hr>
    <div class="word">SERIES</div>
    <div class="sub"><em>Summer/Fall 2025</em>Collection</div>
  </aside>

  <header class="abs masthead">
    <div class="top">COPPER FERN</div>
    <div class="main">PRINTS</div>
    <div class="kit">SAMPLE MERCH KIT</div>
  </header>

  <aside class="abs warning">
    <svg width="50" height="44" viewBox="0 0 50 44" aria-hidden="true"><path d="M25 2 L48 42 H2 Z" fill="none" stroke="var(--alert)" stroke-width="2.5" stroke-linejoin="round"/><line x1="25" y1="15" x2="25" y2="29" stroke="var(--alert)" stroke-width="2.5"/><circle cx="25" cy="35" r="1.8" fill="var(--alert)"/></svg>
    <h3>WARNING</h3>
    <p>These shirts may cause increased shop morale, envy from competitors, and a high volume of customer demand</p>
  </aside>

  <section class="abs gallery">
    <figure class="polaroid"><div class="shot"><div class="garment" role="img" aria-label="Olive t-shirt with a printed vehicle design" style="background:#5d5c45"></div></div></figure>
    <figure class="polaroid"><div class="shot"><div class="garment" role="img" aria-label="Black t-shirt with an off-road truck print" style="background:#0e0e0e"></div></div></figure>
    <figure class="polaroid"><div class="shot"><div class="garment" role="img" aria-label="Royal blue t-shirt with a sunset car print" style="background:#2b3aa6"></div></div></figure>
    <figure class="polaroid"><div class="shot"><div class="garment" role="img" aria-label="Black hoodie with a red channel print" style="background:#151515"></div></div></figure>
  </section>

  <section class="abs contents">
    <h2>MERCH KIT<br>CONTENTS</h2>
    <div class="item"><span class="num">1</span><span>Custom Shop<br>T-shirt</span></div>
    <div class="item"><span class="num">2</span><span>Additional<br>Sample Shirt</span></div>
    <div class="item"><span class="num">3</span><span>CFP Ink<br>Pen</span></div>
  </section>

  <div class="abs divider"></div>

  <section class="abs how">
    <h2>HOW TO START AN ORDER</h2>
    <div class="steps">
      <div class="step">
        <div class="icon"><svg width="24" height="24" viewBox="0 0 24 24" aria-hidden="true"><circle cx="14" cy="10" r="7" fill="none" stroke="var(--ink)" stroke-width="1.5"/><line x1="9" y1="15" x2="3" y2="21" stroke="var(--ink)" stroke-width="2"/></svg></div>
        <div><h3>Choose your ride</h3><p>Send us a picture, or let us know the make and model of the vehicle you would like featured on your apparel</p></div>
      </div>
      <div class="step">
        <div class="icon"><svg width="24" height="24" viewBox="0 0 24 24" aria-hidden="true"><path d="M8 3 L3 6 L5 10 L7 9 V21 H17 V9 L19 10 L21 6 L16 3 Q12 6 8 3 Z" fill="none" stroke="var(--ink)" stroke-width="1.4" stroke-linejoin="round"/></svg></div>
        <div><h3>Pick your gear</h3><p>We will help you choose your t-shirts, sweatshirts or other apparel items and determine sizes and quantities.</p></div>
      </div>
      <div class="step">
        <div class="icon"><svg width="24" height="24" viewBox="0 0 24 24" aria-hidden="true"><line x1="4" y1="20" x2="20" y2="4" stroke="var(--ink)" stroke-width="1.6"/><line x1="4" y1="4" x2="20" y2="20" stroke="var(--ink)" stroke-width="1.6"/><circle cx="4.5" cy="4.5" r="2.5" fill="none" stroke="var(--ink)" stroke-width="1.4"/></svg></div>
        <div><h3>We customize</h3><p>We make the magic happen and our team of expert artists will design your shirts and get a proof out to you. Upon order approval your order will go into production.</p></div>
      </div>
    </div>
  </section>

  <section class="abs about">
    <h2>About us</h2>
    <p>Copper Fern Prints is a second-generation screen printing company in Millbrook, VT. For over 45 years, we’ve specialized in high-quality custom apparel and merchandise.</p>
  </section>

  <section class="abs fine-print">
    <h3>THE FINE PRINT:</h3>
    <p>lease send high-resolution photos of vehicles. When sending additional logos, please send vector images. Note that our shop minimum is 24 pieces for one-color prints and 100 pieces for full-color screen print. We also promise accurate, quality work.</p>
  </section>
  <div class="abs page-curl"></div>

  <section class="abs contact">
    <h3>CONTACT<br>CFP SALES</h3>
    <p>For more information,<br>email us at</p>
    <div class="line"><svg width="14" height="10" viewBox="0 0 14 10" aria-hidden="true"><rect width="14" height="10" fill="var(--ink)"/><path d="M0 0 L7 6 L14 0" fill="none" stroke="var(--sheet)" stroke-width="1.2"/></svg>hello@copperfernprints.com</div>
    <div class="line"><svg width="14" height="14" viewBox="0 0 24 24" aria-hidden="true"><path d="M6 2 L10 7 L8 10 Q10 14 14 16 L17 14 L22 18 L19 22 Q10 22 4 12 Q2 7 6 2 Z" fill="var(--ink)"/></svg>555-318-2047</div>
  </section>

  <div class="abs brand-mark"><div class="square"></div>Copper Fern Prints</div>

  <div class="abs sign-line"></div>
  <p class="abs sign-off">We look forward to working with you!</p>

</main>
</body>
</html>
```